Cover Page for Financial Statements

We need a cover page designed for our Financial Statements. It will need to include our business logo and the Chartered accountant logo.
We have included our current title page ( image titled full.png ) to show all the information that is needed to be included such as the title 'Financial Statements' and 'The year ended March 2023'. We would like to see designs that reflect our logo but also adds some interest with objects / deisngs that fill up more of the page.

Industry/Entity Type

Accounting

Font styles to use
Serif
Sans Serif

Colors

Designer to choose only greyscale colors for use in the design.

Requirements
Must have
• - A4 document size, our logo, Chartered Accountant Logo
Should not have
• Bright Colors

```html
<!DOCTYPE html>
<html lang="en">
<head>
<meta charset="UTF-8">
<title>Clearline Accounting &amp; Advisory Limited – Financial Statements 2023</title>
<link href="https://fonts.googleapis.com/css2?family=Lexend:wght@300;400;500;600&family=Josefin+Sans:wght@400&display=swap" rel="stylesheet">
<style>
  :root {
    --ink: #111111;
    --paper: #ffffff;
    --mist: #ececec;
    --mist-soft: #f6f6f6;
    --chart: #dedede;
    --chart-line: #d2d2d2;
    --photo-dark: #151515;
    --photo-mid: #3a3a3a;
    --badge: #8c8c8c;
    --badge-text: #333333;
  }
  * { margin: 0; padding: 0; box-sizing: border-box; }
  html, body { width: 848px; height: 1200px; overflow: hidden; background: var(--paper); }
  .cover {
    position: relative;
    width: 848px;
    height: 1200px;
    background: var(--paper);
    font-family: "Lexend", sans-serif;
    color: var(--ink);
    overflow: hidden;
  }
  .backdrop-band {
    position: absolute;
    left: 0; top: 205px;
    width: 848px; height: 525px;
    background: linear-gradient(180deg, var(--paper) 0%, var(--mist-soft) 12%, var(--mist) 55%, var(--mist-soft) 88%, var(--paper) 100%);
  }
  .backdrop-chart {
    position: absolute;
    left: 0; top: 205px;
    width: 848px; height: 525px;
  }
  .brand {
    position: absolute;
    left: 0; top: 104px;
    width: 848px;
    display: flex;
    justify-content: center;
    align-items: center;
    gap: 16px;
  }
  .brand-mark { width: 14px; height: 14px; background: var(--ink); }
  .brand-name {
    font-family: "Josefin Sans", sans-serif;
    font-weight: 400;
    font-size: 44px;
    letter-spacing: 6px;
    color: var(--ink);
    line-height: 1;
  }
  .feature-frame {
    position: absolute;
    left: 81px; top: 237px;
    width: 687px; height: 447px;
    border: 2px solid var(--ink);
    background: var(--paper);
  }
  .corner { position: absolute; width: 34px; height: 34px; background: var(--ink); }
  .corner-top-left { left: -2px; top: -2px; }
  .corner-bottom-right { right: -2px; bottom: -2px; }
  .feature-photo {
    position: absolute;
    left: 31px; top: 39px;
    width: 624px; height: 374px;
    border: 2px solid var(--ink);
    background: radial-gradient(ellipse at 55% 45%, var(--photo-mid) 0%, var(--photo-dark) 70%);
  }
  .company-name {
    position: absolute;
    left: 69px; top: 762px;
    font-size: 31px;
    font-weight: 500;
    line-height: 38px;
    text-transform: uppercase;
  }
  .document-title {
    position: absolute;
    left: 69px; top: 868px;
    font-size: 20px;
    font-weight: 500;
    letter-spacing: 1px;
  }
  .period {
    position: absolute;
    left: 66px; top: 982px;
  }
  .period-label { font-size: 25px; font-weight: 300; letter-spacing: 0.5px; }
  .period-label strong { font-weight: 500; }
  .period-date { margin-top: 14px; margin-left: 3px; font-size: 27px; font-weight: 400; line-height: 1; }
  .period-date sup { font-size: 12px; vertical-align: 12px; }
  .period-year { margin-left: 3px; margin-top: 4px; font-size: 50px; font-weight: 600; line-height: 1.1; }
  .accreditation {
    position: absolute;
    left: 560px; top: 966px;
    width: 200px;
    display: flex;
    flex-direction: column;
    align-items: center;
  }
  .accreditation-badge {
    width: 72px; height: 72px;
    border-radius: 50%;
    background: var(--badge);
  }
  .accreditation-name {
    margin-top: 14px;
    font-size: 12px;
    font-weight: 500;
    letter-spacing: 1px;
    color: var(--badge-text);
    text-align: center;
    line-height: 15px;
  }
  .accreditation-name small { font-size: 8px; letter-spacing: 0.8px; }
  .corner-block {
    position: absolute;
    left: 578px; top: 1108px;
    width: 200px; height: 92px;
    background: var(--ink);
  }
</style>
</head>
<body>
<main class="cover">
  <div class="backdrop-band"></div>

  <svg class="backdrop-chart" viewBox="0 0 848 525" aria-hidden="true">
    <g fill="var(--chart)">
      <rect x="0" y="380" width="8" height="145"/>
      <rect x="14" y="340" width="10" height="185"/>
      <rect x="30" y="310" width="12" height="215"/>
      <rect x="48" y="360" width="8" height="165"/>
      <rect x="60" y="395" width="10" height="130"/>
      <rect x="778" y="270" width="12" height="255"/>
      <rect x="796" y="120" width="14" height="405"/>
      <rect x="816" y="230" width="10" height="295"/>
      <rect x="832" y="150" width="12" height="375"/>
    </g>
    <g fill="var(--chart)" opacity="0.7">
      <rect x="100" y="490" width="4" height="35"/><rect x="150" y="495" width="4" height="30"/>
      <rect x="200" y="488" width="4" height="37"/><rect x="250" y="494" width="4" height="31"/>
      <rect x="300" y="490" width="4" height="35"/><rect x="350" y="496" width="4" height="29"/>
      <rect x="400" y="489" width="4" height="36"/><rect x="450" y="494" width="4" height="31"/>
      <rect x="500" y="490" width="4" height="35"/><rect x="550" y="495" width="4" height="30"/>
      <rect x="600" y="488" width="4" height="37"/><rect x="650" y="494" width="4" height="31"/>
      <rect x="700" y="490" width="4" height="35"/><rect x="750" y="495" width="4" height="30"/>
    </g>
    <g stroke="var(--chart-line)" stroke-width="1.5" fill="none">
      <polyline points="0,355 24,335 80,390"/>
      <polyline points="0,495 24,470 80,510"/>
      <polyline points="770,210 810,140 848,105"/>
    </g>
    <g fill="var(--chart-line)">
      <circle cx="24" cy="335" r="4"/>
      <circle cx="24" cy="470" r="4"/>
      <circle cx="810" cy="140" r="4"/>
    </g>
  </svg>

  <header class="brand">
    <span class="brand-mark"></span>
    <span class="brand-name">CLEARLINE</span>
  </header>

  <section class="feature-frame">
    <span class="corner corner-top-left"></span>
    <div class="feature-photo" role="img" aria-label="Monochrome photo of a hand touching a glowing network of digital finance icons above a keyboard"></div>
    <span class="corner corner-bottom-right"></span>
  </section>

  <h1 class="company-name">Clearline Accounting &amp;<br>Advisory Limited</h1>
  <h2 class="document-title">FINANCIAL STATEMENTS</h2>

  <div class="period">
    <p class="period-label">FOR THE <strong>YEAR ENDED</strong></p>
    <p class="period-date">31<sup>ST</sup> MARCH</p>
    <p class="period-year">2023</p>
  </div>

  <div class="accreditation">
    <span class="accreditation-badge"></span>
    <p class="accreditation-name">MERIDIAN ACCOUNTANTS<br><small>GUILD OF PRACTICE</small></p>
  </div>
  <div class="corner-block"></div>
</main>
</body>
</html>
```